TechNurse Atlantic
TechNurse Atlantic - Computers
Creative Brief
Professional
Derwin Halcott Jr., MCP
Partner
47 Marlow Lane Hamilton HM11, Suite 208 Caldera Isles
dhalcott@wirelunabda.com
http://www.wirelunabda.com
Please note that #21 is the winning logo for TechNurse. Please design stationary based on this, thanks. http://orders.brandquillhub.com/contests/technurse-atlantic

```html
<!DOCTYPE html>
<html lang="en">
<head>
<meta charset="utf-8">
<title>TechNurse Atlantic — Stationery</title>
<link href="https://fonts.googleapis.com/css2?family=Roboto:wght@400;500;700;900&display=swap" rel="stylesheet">
<style>
:root{
  --bg:#e8e5e1;
  --paper:#ffffff;
  --ink:#2b2b2b;
  --muted:#6d6d6d;
  --brand:#8e1b22;
  --brand-dark:#4a0a0e;
  --brand-bright:#c4262f;
  --stripe:#c9c9c9;
  --faint:#ececec;
  --fold:#e4e4e4;
}
*{box-sizing:border-box;margin:0;padding:0}
html,body{width:1200px;height:935px;overflow:hidden}
body{background:var(--bg);font-family:"Roboto",Arial,sans-serif;color:var(--ink);position:relative}
.defs{position:absolute;width:0;height:0}
.piece{position:absolute;background:var(--paper);box-shadow:0 4px 14px rgba(0,0,0,.18);overflow:hidden}
.wave{position:absolute;left:0;bottom:0;width:100%}
.brand{display:flex;align-items:center;gap:6px;font-weight:900;color:var(--brand);letter-spacing:.5px;white-space:nowrap}
.brand .dot{display:inline-block;border-radius:50%;background:var(--brand);flex:none}
.web{position:absolute;color:#fff;font-weight:700;white-space:nowrap}
.addr{position:absolute;color:var(--ink);line-height:1.45;white-space:nowrap}

/* fax sheet */
.fax{left:30px;top:208px;width:400px;height:518px}
.fax .brand{position:absolute;left:26px;top:28px;font-size:22px}
.fax .brand .dot{width:14px;height:14px}
.fax-title{position:absolute;left:26px;top:108px;font-size:30px;font-weight:700}
.fax-fields{position:absolute;left:26px;top:170px;width:340px;list-style:none}
.fax-fields li{display:flex;align-items:flex-end;height:32px;font-size:10px;font-weight:700}
.fax-fields li span{width:50px}
.fax-fields li i{flex:1;border-bottom:1px dotted #999;height:1px}
.fax-checks{position:absolute;left:26px;top:318px;display:flex;gap:26px;font-size:10px}
.fax-checks label{display:flex;align-items:center;gap:6px}
.fax-checks b{width:9px;height:9px;border:1px solid #888;display:inline-block}
.fax .addr{left:26px;bottom:84px;font-size:9px}
.fax .web{right:22px;bottom:16px;font-size:10px}

/* letterhead */
.letter{left:450px;top:208px;width:400px;height:518px}
.letter .brand{position:absolute;left:26px;top:28px;font-size:22px}
.letter .brand .dot{width:14px;height:14px}
.letter-mark{position:absolute;left:0;right:0;top:200px;text-align:center;font-size:58px;font-weight:900;color:var(--faint)}
.letter .addr{left:26px;bottom:92px;font-size:9px}
.letter .web{right:22px;bottom:18px;font-size:10px}

/* envelope */
.envelope{left:870px;top:208px;width:310px;height:150px}
.envelope .flap{position:absolute;left:0;top:0;width:100%;height:40px}
.envelope .brand{position:absolute;left:22px;top:44px;font-size:16px}
.envelope .brand .dot{width:10px;height:10px}
.envelope .addr{left:22px;top:68px;font-size:7px}
.envelope .web{right:14px;bottom:8px;font-size:8px}

/* business cards */
.card{width:270px;height:154px}
.card-front{left:890px;top:400px}
.card-back{left:890px;top:572px;background:radial-gradient(circle at 50% 45%,var(--brand-bright),var(--brand) 55%,var(--brand-dark))}
.card-person{position:absolute;left:16px;top:16px}
.card-person h2{font-size:10px;font-weight:700}
.card-person p{font-size:8px;color:var(--muted)}
.card-front .addr{left:16px;top:52px;font-size:7px}
.card-front .brand{position:absolute;right:14px;top:22px;font-size:14px}
.card-front .brand .dot{width:9px;height:9px}
.card-front .web{right:12px;bottom:8px;font-size:7px}
.card-back .brand{position:absolute;left:0;right:0;top:62px;justify-content:center;font-size:22px;color:#fff}
.card-back .brand .dot{width:14px;height:14px;background:#fff}
</style>
</head>
<body>

<svg class="defs" aria-hidden="true">
  <defs>
    <linearGradient id="redBand" x1="0" y1="0" x2="1" y2="0">
      <stop offset="0" stop-color="#3d070a"/>
      <stop offset=".55" stop-color="#a01e26"/>
      <stop offset="1" stop-color="#5a0b10"/>
    </linearGradient>
  </defs>
</svg>

<!-- Fax sheet -->
<section class="piece fax">
  <div class="brand"><span class="dot"></span>TechNurse</div>
  <h1 class="fax-title">FAX</h1>
  <ul class="fax-fields">
    <li><span>To :</span><i></i></li>
    <li><span>Fax :</span><i></i></li>
    <li><span>Phone :</span><i></i></li>
    <li><span>Re :</span><i></i></li>
  </ul>
  <div class="fax-checks">
    <label><b></b>Urgent</label>
    <label><b></b>For Review</label>
    <label><b></b>Please Reply</label>
  </div>
  <p class="addr">47 Marlow Lane Westbrook WB22, Suite 208, Caldera Isles<br>P. (441) 290-1836 | C. (441) 533-6021<br>E. dhalcott@wirelunabda.com</p>
  <svg class="wave" viewBox="0 0 400 80" height="80" preserveAspectRatio="none" aria-hidden="true">
    <path d="M0 30 C120 -4 250 62 400 14 V80 H0Z" fill="var(--stripe)"/>
    <path d="M0 38 C125 6 255 70 400 22 V80 H0Z" fill="#fff"/>
    <path d="M0 44 C130 14 260 76 400 30 V80 H0Z" fill="url(#redBand)"/>
  </svg>
  <span class="web">www.wirelunabda.com</span>
</section>

<!-- Letterhead -->
<section class="piece letter">
  <div class="brand"><span class="dot"></span>TechNurse</div>
  <div class="letter-mark" aria-hidden="true">TechNurse</div>
  <p class="addr">47 Marlow Lane Westbrook WB22, Suite 208, Caldera Isles<br>P. (441) 290-1836 | C. (441) 533-6021<br>E. dhalcott@wirelunabda.com</p>
  <svg class="wave" viewBox="0 0 400 80" height="80" preserveAspectRatio="none" aria-hidden="true">
    <path d="M0 30 C120 -4 250 62 400 14 V80 H0Z" fill="var(--stripe)"/>
    <path d="M0 38 C125 6 255 70 400 22 V80 H0Z" fill="#fff"/>
    <path d="M0 44 C130 14 260 76 400 30 V80 H0Z" fill="url(#redBand)"/>
  </svg>
  <span class="web">www.wirelunabda.com</span>
</section>

<!-- Envelope -->
<section class="piece envelope">
  <svg class="flap" viewBox="0 0 310 40" preserveAspectRatio="none" aria-hidden="true">
    <path d="M0 0 L155 34 L310 0" fill="none" stroke="var(--fold)" stroke-width="1"/>
  </svg>
  <div class="brand"><span class="dot"></span>TechNurse</div>
  <p class="addr">47 Marlow Lane<br>Westbrook WB22, Suite 208<br>Caldera Isles</p>
  <svg class="wave" viewBox="0 0 310 40" height="40" preserveAspectRatio="none" aria-hidden="true">
    <path d="M0 14 C90 -2 200 30 310 4 V40 H0Z" fill="var(--stripe)"/>
    <path d="M0 18 C95 2 205 34 310 8 V40 H0Z" fill="#fff"/>
    <path d="M0 21 C100 6 210 38 310 12 V40 H0Z" fill="url(#redBand)"/>
  </svg>
  <span class="web">www.wirelunabda.com</span>
</section>

<!-- Business card front -->
<section class="piece card card-front">
  <div class="card-person">
    <h2>Derwin Halcott, CSP</h2>
    <p>Partner</p>
  </div>
  <p class="addr">47 Marlow Lane<br>Westbrook WB22, Suite 208<br>Caldera Isles<br>P. (441) 290-1836<br>C. (441) 533-6021<br>E. dhalcott@wirelunabda.com</p>
  <div class="brand"><span class="dot"></span>TechNurse</div>
  <svg class="wave" viewBox="0 0 270 36" height="36" preserveAspectRatio="none" aria-hidden="true">
    <path d="M0 12 C80 -2 170 28 270 4 V36 H0Z" fill="var(--stripe)"/>
    <path d="M0 16 C85 2 175 32 270 8 V36 H0Z" fill="#fff"/>
    <path d="M0 19 C90 6 180 36 270 12 V36 H0Z" fill="url(#redBand)"/>
  </svg>
  <span class="web">www.wirelunabda.com</span>
</section>

<!-- Business card back -->
<section class="piece card card-back">
  <div class="brand"><span class="dot"></span>TechNurse</div>
</section>

</body>
</html>
```